High-end dermatology office brochure design

Corvella Skin and Laser is a high-end dermatology practice that specializes in custom skin care solutions, and skin cancer surveillance and treatment. Brochure should be elegant, but informative to attract high-end customers.

Target Market(s)

Men and women 27-60

Industry/Entity Type

Office

Requirements
Must have
• Attached document has required copy, including, websites, address and company phone number
Nice to have
• images

```html
<!DOCTYPE html>
<html lang="en">
<head>
<meta charset="utf-8">
<title>Visit Our Locations – Corvella Skin and Laser</title>
<link rel="stylesheet" href="https://fonts.googleapis.com/css2?family=Caveat:wght@400&family=Open+Sans:wght@300;400&family=Arimo:wght@400&display=swap">
<style>
  :root {
    --tile: #f1d9d2;
    --tile-soft: #f7e9e5;
    --paper: #ffffff;
    --accent: #dea290;
    --card: #f8ece8;
    --ring: #efd3ca;
    --map-light: #ecebe4;
    --map-mid: #dcdad0;
    --ink: #222222;
  }
  html, body {
    margin: 0;
    padding: 0;
    width: 1200px;
    height: 1200px;
    overflow: hidden;
    background: var(--paper);
  }
  .page {
    position: relative;
    width: 1200px;
    height: 1200px;
    overflow: hidden;
    background: var(--paper);
  }
  .tile-grid {
    position: absolute;
    left: 2px;
    top: 0;
    display: grid;
    grid-template-columns: repeat(4, 127px);
    grid-auto-rows: 127px;
    gap: 7px;
  }
  .tile {
    border-radius: 5px;
    background: linear-gradient(135deg, var(--tile-soft), var(--tile));
  }
  .tile-fade {
    position: absolute;
    inset: 0;
    background:
      linear-gradient(to bottom, rgba(255,255,255,1) 0%, rgba(255,255,255,0.55) 22%, rgba(255,255,255,0) 45%),
      linear-gradient(to right, rgba(255,255,255,0) 0%, rgba(255,255,255,0.25) 14%, rgba(255,255,255,0.85) 34%, rgba(255,255,255,1) 46%);
  }
  .section-title {
    position: absolute;
    left: 0;
    width: 1184px;
    top: 455px;
    margin: 0;
    text-align: center;
    font-family: "Caveat", cursive;
    font-weight: 400;
    font-size: 64px;
    letter-spacing: 3px;
    word-spacing: 8px;
    color: var(--accent);
  }
  .location {
    position: absolute;
    top: 537px;
    width: 240px;
    text-align: center;
    font-family: "Arimo", Arial, sans-serif;
    color: var(--ink);
  }
  .location--phoenix { left: 247px; }
  .location--scottsdale { left: 480px; }
  .location--honolulu { left: 713px; }
  .location__city {
    margin: 0 0 11px;
    font-size: 16.5px;
    font-weight: 400;
    height: 18px;
  }
  .map-card {
    margin: 0 auto;
    width: 228px;
    height: 228px;
    border-radius: 8px;
    background: var(--card);
    box-shadow: 0 2px 6px rgba(190,150,140,0.25);
    display: flex;
    align-items: center;
    justify-content: center;
  }
  .map-disc {
    width: 203px;
    height: 203px;
    border-radius: 50%;
    border: 5px solid var(--ring);
    background: radial-gradient(circle at 45% 40%, var(--map-light), var(--map-mid));
  }
  .location__address {
    margin: 16px 0 0;
    font-style: normal;
    font-size: 15.5px;
    line-height: 19.4px;
  }
  .contact {
    position: absolute;
    left: 0;
    width: 1200px;
    top: 1026px;
    text-align: center;
    color: var(--ink);
  }
  .contact__phone {
    margin: 0;
    font-family: "Arimo", Arial, sans-serif;
    font-size: 23px;
    line-height: 30px;
  }
  .contact__web {
    margin: 0;
    font-family: "Open Sans", Arial, sans-serif;
    font-weight: 400;
    font-size: 21px;
    line-height: 30px;
  }
</style>
</head>
<body>
<main class="page">
  <div class="tile-grid" aria-hidden="true">
    <div class="tile"></div><div class="tile"></div><div class="tile"></div><div class="tile"></div>
    <div class="tile"></div><div class="tile"></div><div class="tile"></div><div class="tile"></div>
    <div class="tile"></div><div class="tile"></div><div class="tile"></div><div class="tile"></div>
    <div class="tile"></div><div class="tile"></div><div class="tile"></div><div class="tile"></div>
    <div class="tile"></div><div class="tile"></div><div class="tile"></div><div class="tile"></div>
    <div class="tile"></div><div class="tile"></div><div class="tile"></div><div class="tile"></div>
    <div class="tile"></div><div class="tile"></div><div class="tile"></div><div class="tile"></div>
    <div class="tile"></div><div class="tile"></div><div class="tile"></div><div class="tile"></div>
    <div class="tile"></div><div class="tile"></div><div class="tile"></div><div class="tile"></div>
  </div>
  <div class="tile-fade" aria-hidden="true"></div>

  <h1 class="section-title">Visit Our Locations</h1>

  <section class="location location--phoenix">
    <h2 class="location__city">Phoenix, Arizona</h2>
    <div class="map-card">
      <div class="map-disc" role="img" aria-label="Street map of the Phoenix office location"></div>
    </div>
    <address class="location__address">
      Corvella Skin and Laser<br>
      4170 E Mesquite Rd<br>
      Building #9<br>
      Suite #148<br>
      Phoenix, AZ 85044
    </address>
  </section>

  <section class="location location--scottsdale">
    <h2 class="location__city">Scottsdale,&nbsp; Arizona</h2>
    <div class="map-card">
      <div class="map-disc" role="img" aria-label="Street map of the Scottsdale office location"></div>
    </div>
    <address class="location__address">
      Verdant Skin Solutions<br>
      Located in Wellspring Commons<br>
      9240 E Canyon Cove<br>
      Suite #103<br>
      Scottsdale, Az 85260
    </address>
  </section>

  <section class="location location--honolulu">
    <h2 class="location__city">Honolulu, Hawaii</h2>
    <div class="map-card">
      <div class="map-disc" role="img" aria-label="Street map of the Honolulu office location"></div>
    </div>
    <address class="location__address">
      Island Skin Cancer Center<br>
      Harborline Plaza<br>
      Suite #470<br>
      620 Kaiolu Blvd.<br>
      Honolulu, HI 96813
    </address>
  </section>

  <footer class="contact">
    <p class="contact__phone">480-555-0182</p>
    <p class="contact__web">corvellaskincare.com</p>
    <p class="contact__web">Shop at 2cherishyourskin.com</p>
  </footer>
</main>
</body>
</html>
```